Flyer-Design für Vermietung und Verkauf von Palettenmöbeln
Zielgruppe
Ich vermiete und verkaufe in Tischler-Handarbeit hergestellte Palettenmöbel aus recycelten Paletten, wobei mein Schwerpunkt bei der Vermietung liegt. Meine Zielgruppe sind alle, die Veranstaltungen, Events , Messen, Präsentationen, private Feiern und Ähnliches planen und organisieren. Große und kleine Firmen, senatseigene Stellen, Privatpersonen, aber der Schwerpunkt liegt bei den Eventagenturen, welche mit der Organisation verschiedenster Veranstaltungen beauftragt werden.
Aufgabenstellung
Ich hätte ein klares und modernes Design mit BÄHM-Charakter. Der Flyer soll ein Hingucker sein, aber den Betrachter nicht erschlagen. Das Thema Nachhaltigkeit (die Möbel sind aus recylten Paletten) sollte bedacht werden. Ich hätte gern einen Faltflyer in DIN lang Größe. Dies ist für einen Mailing-Versand besser geeignet. Ich liefere eigene Bilder, aber sollten ein Stock-Bilder hilfreich sein, können dies gern verwendet werden. Ich habe natürlich noch mehr Bilder und kann diese gern zur Verfügung stellen, wenn ich weiß was benötigt wird. Es soll nicht viel Text in den Flyer. Ich bin hier sehr dankbar für Vorschläge, da ich mich mit dem Text sehr schwer tue. Ich hoffe, die Profis können mir auch beim Text helfen. Ich stelle auch Fotos meines alten Flyer zur Verfügung. Dieser ist definitv zu konservativ, langweilig und veraltet. Ich brauche ein modernes, hippes Design mit überzeugendem Text.

```html
<!DOCTYPE html>
<html lang="de">
<head>
<meta charset="utf-8">
<title>Palettenlounge – Faltflyer DIN lang</title>
<link rel="stylesheet" href="https://fonts.googleapis.com/css2?family=Montserrat:wght@400;500;600;700&display=swap">
<style>
  :root {
    --green: #5cb531;
    --green-dark: #4a9a24;
    --ink: #3b3b3b;
    --ink-soft: #5a5a5a;
    --paper: #ffffff;
    --stage: #e9eaeb;
    --fold: #ececec;
  }
  * { box-sizing: border-box; margin: 0; padding: 0; }
  html, body { width: 1200px; height: 1200px; overflow: hidden; }
  body {
    background: var(--stage);
    font-family: "Montserrat", Arial, sans-serif;
    color: var(--ink);
    position: relative;
  }
  .flyer {
    position: absolute;
    left: 42px; top: 206px;
    width: 1116px; height: 788px;
    display: flex;
    background: var(--paper);
    box-shadow: 0 10px 30px rgba(0,0,0,0.12);
  }
  .panel {
    position: relative;
    width: 372px; height: 100%;
    overflow: hidden;
  }
  .panel + .panel { border-left: 1px solid var(--fold); }

  .photo { position: absolute; }
  .label {
    position: absolute;
    display: inline-block;
    font-weight: 500;
    text-transform: uppercase;
    line-height: 1;
    white-space: nowrap;
  }
  .label--green { background: var(--green); color: #fff; }
  .label--white { background: #fff; color: var(--green); }

  .rule { position: absolute; width: 3px; background: var(--green); }

  .kicker { color: var(--green); font-weight: 600; font-size: 12px; letter-spacing: .04em; text-transform: uppercase; }
  .body-text { font-size: 11.5px; line-height: 1.55; color: var(--ink-soft); }
  .amp { color: var(--green); }

  /* Panel 1 – Über uns */
  .panel--about .photo { left: 34px; top: 34px; width: 304px; height: 300px;
    background: linear-gradient(160deg, #8a8f96 0%, #a9825a 45%, #d2ab7c 75%, #7a5a3c 100%); }
  .panel--about .label-a { left: 26px; top: 232px; font-size: 30px; padding: 6px 10px; }
  .panel--about .label-b { left: 26px; top: 276px; font-size: 15px; padding: 5px 10px; }
  .about-text { position: absolute; left: 34px; top: 370px; width: 304px; }
  .about-text h2 { font-size: 19px; font-weight: 500; line-height: 1.3; margin: 12px 0 14px; color: var(--ink); }
  .about-text h3 { font-size: 11.5px; font-weight: 700; margin: 12px 0 4px; color: var(--ink); }
  .panel--about .rule { left: 34px; top: 660px; height: 90px; }
  .about-note { position: absolute; left: 54px; top: 666px; width: 160px; color: var(--green); font-weight: 700; font-size: 12px; line-height: 1.5; }
  .plant { position: absolute; left: 236px; top: 648px; width: 120px; height: 126px;
    border-radius: 8px;
    background: linear-gradient(180deg, #5faa2e 0%, #4a9526 55%, #f1f1f1 56%, #e2e2e2 100%); }

  /* Panel 2 – Kontakt */
  .panel--contact .rule { left: 34px; top: 34px; height: 60px; }
  .kicker--contact { position: absolute; right: 46px; top: 72px; font-size: 14px; }
  .panel--contact .photo { left: 34px; top: 120px; width: 304px; height: 220px;
    background: linear-gradient(135deg, #d7d8d9 0%, #c4c5c6 50%, #9d9ea0 100%); }
  .panel--contact .label-name { left: 34px; top: 140px; font-size: 15px; padding: 5px 10px; }
  .label-role { position: absolute; left: 44px; top: 169px; font-size: 11px; color: #fff; }
  .questions { position: absolute; left: 34px; top: 390px; width: 300px; }
  .questions .label-q { position: relative; font-size: 15px; padding: 5px 10px; }
  .questions .big { font-size: 30px; font-weight: 500; letter-spacing: .02em; margin-top: 4px; color: var(--ink); }
  .questions .body-text { margin-top: 10px; }
  .brand { display: flex; align-items: center; gap: 8px; color: var(--green); font-weight: 700; }
  .brand-mark { width: 14px; height: 14px; background: var(--green); }
  .contact-block { position: absolute; left: 34px; top: 560px; }
  .contact-block .brand { font-size: 20px; margin-bottom: 18px; }
  .address { font-size: 12.5px; line-height: 1.5; color: var(--ink); }
  .address strong { font-size: 14px; font-weight: 600; }
  .address .tag { color: var(--green); font-weight: 700; }
  .url { color: var(--green); font-weight: 700; font-size: 12.5px; }
  .contact-block .url { display: block; margin-top: 18px; }

  /* Panel 3 – Titel */
  .panel--cover .brand { position: absolute; right: 34px; top: 60px; font-size: 28px; }
  .panel--cover .brand-mark { width: 22px; height: 22px; }
  .panel--cover .photo { left: 34px; top: 150px; width: 338px; height: 420px;
    background: linear-gradient(180deg, #9ea3a6 0%, #b89b78 40%, #c9a57a 55%, #4f9b2b 78%, #3c8420 100%); }
  .cover-labels { position: absolute; left: 50px; top: 450px; }
  .cover-labels .label { position: relative; display: table; }
  .cover-labels .l1 { font-size: 31px; padding: 6px 10px; }
  .cover-labels .l2, .cover-labels .l3 { font-size: 17px; padding: 5px 10px; margin-top: 4px; }
  .panel--cover .rule { left: 34px; top: 610px; height: 90px; }
  .tagline { position: absolute; left: 56px; top: 616px; }
  .tagline .main { font-size: 27px; font-weight: 400; color: var(--ink); }
  .tagline .sub { font-size: 15px; color: var(--ink-soft); margin-top: 4px; }
  .panel--cover .url { position: absolute; right: 34px; top: 730px; }
</style>
</head>
<body>
  <main class="flyer">
    <section class="panel panel--about">
      <div class="photo" role="img" aria-label="Foto: Palettenmöbel als Weinpräsentation auf einer Messe"></div>
      <span class="label label--green label-a">Vielfältig</span>
      <span class="label label--white label-b">Einsetzbar</span>
      <div class="about-text">
        <p class="kicker">Über uns</p>
        <h2>Wir verkaufen <span class="amp">&amp;</span> vermieten hochwertige handgefertigte Möbel aus Europaletten</h2>
        <p class="body-text">Machen Sie Ihr Firmenevent oder Ihre private Feier zu einem Erlebnis mit hochwertigen handgefertigten Palettenmöbeln.</p>
        <h3>Der Umwelt zuliebe</h3>
        <p class="body-text">In einer Welt, in der Nachhaltigkeit eine immer größere Rolle spielt, erhalten Sie bei uns Lounge-Möbel aus recycelten Europaletten.</p>
      </div>
      <div class="rule"></div>
      <p class="about-note">Wir vermieten und<br>liefern in Berlin und in<br>der nahen Umgebung</p>
      <div class="plant" role="img" aria-label="Grünpflanze im weißen Topf"></div>
    </section>

    <section class="panel panel--contact">
      <div class="rule"></div>
      <p class="kicker kicker--contact">Kontakt</p>
      <div class="photo" role="img" aria-label="Porträtfoto der Inhaberin"></div>
      <span class="label label--white label-name">Greta Holmberg</span>
      <span class="label-role">Inhaberin</span>
      <div class="questions">
        <span class="label label--green label-q">Sie haben</span>
        <p class="big">FRAGEN<span class="amp">?</span></p>
        <p class="body-text">Wir beraten Sie gerne!<br>Für mehr Informationen besuchen<br>Sie uns gerne auch online.</p>
      </div>
      <div class="contact-block">
        <div class="brand"><span class="brand-mark"></span>Palettenlounge</div>
        <p class="address">
          <strong>Greta Holmberg</strong><br>
          Lindenweg 14<br>
          10115 Berlin<br><br>
          <span class="tag">T.</span> +49 (0) 170 5550182<br>
          <span class="tag">E.</span> info@palettenlounge.de
        </p>
        <span class="url">www.palettenlounge.de</span>
      </div>
    </section>

    <section class="panel panel--cover">
      <div class="brand"><span class="brand-mark"></span>Palettenlounge</div>
      <div class="photo" role="img" aria-label="Foto: Lounge mit Palettenmöbeln auf Kunstrasen in einer Halle"></div>
      <div class="cover-labels">
        <span class="label label--green l1">Loungemöbel</span>
        <span class="label label--white l2">Aus recycelten</span>
        <span class="label label--white l3">Europaletten</span>
      </div>
      <div class="rule"></div>
      <div class="tagline">
        <p class="main">Vermietung <span class="amp">&amp;</span> Verkauf</p>
        <p class="sub">in Berlin und Umgebung</p>
      </div>
      <span class="url">www.palettenlounge.de</span>
    </section>
  </main>
</body>
</html>
```